Tamsen Health Guides
Your Personal Medical Record
Tamsen Health Guides - Medical
Creative Brief
Professional
Gareth L. Pomroy
MD
4271 Copper Finch Avenue Denver, Colorado 80219
garethlpomroy@mailvessel.example
mytamsen.example
I need the business card to include the scan icon for smart phone users to access the website from the business card.
SiteAdmin SiteAdmin

```html
<!DOCTYPE html>
<html lang="en">
<head>
<meta charset="utf-8">
<title>Tamsen Health Guides – Business Card</title>
<link href="https://fonts.googleapis.com/css2?family=Open+Sans:wght@400;600;700&display=swap" rel="stylesheet">
<style>
  :root {
    --backdrop: #e9e7ee;
    --card-white: #ffffff;
    --brand-purple: #33229a;
    --brand-purple-dark: #23176e;
    --band-light: #3d2ba8;
    --ink-white: #ffffff;
    --tag-ink: #2a1f7a;
  }
  * { margin: 0; padding: 0; box-sizing: border-box; }
  html, body {
    width: 1200px; height: 902px; overflow: hidden;
    background: var(--backdrop);
    font-family: "Open Sans", Arial, sans-serif;
  }
  .card {
    position: absolute; left: 100px; top: 165px;
    width: 1000px; height: 572px;
    background: var(--card-white);
    box-shadow: 0 10px 30px rgba(0,0,0,0.18);
    overflow: hidden;
  }
  .brand {
    position: absolute; left: 300px; top: 70px;
    width: 400px; text-align: center;
  }
  .brand-mark {
    display: flex; align-items: center; justify-content: center; gap: 12px;
  }
  .brand-square {
    width: 26px; height: 26px; background: var(--brand-purple);
  }
  .brand-name {
    font-size: 34px; font-weight: 600; color: var(--brand-purple);
    letter-spacing: -0.5px;
  }
  .brand-tagline {
    margin-top: 6px;
    font-size: 17px; font-weight: 600; color: var(--tag-ink);
    letter-spacing: 1.4px;
  }
  .band {
    position: absolute; left: 0; top: 205px;
    width: 100%; height: 190px;
    background: linear-gradient(90deg, var(--brand-purple-dark) 0%, var(--band-light) 35%, var(--brand-purple) 100%);
  }
  .holder {
    position: absolute; left: 40px; top: 90px; color: var(--ink-white);
  }
  .holder-name { font-size: 20px; font-weight: 700; }
  .holder-title { margin-top: 8px; font-size: 16px; }
  .contact {
    position: absolute; left: 560px; top: 22px;
    list-style: none; color: var(--ink-white); font-size: 16px;
  }
  .contact li {
    display: flex; align-items: flex-start; gap: 10px; margin-bottom: 7px; line-height: 1.35;
  }
  .contact svg { flex: 0 0 18px; margin-top: 2px; }
</style>
</head>
<body>
  <div class="card">
    <div class="brand">
      <div class="brand-mark">
        <span class="brand-square"></span>
        <span class="brand-name">Tamsen Health Guides</span>
      </div>
      <p class="brand-tagline">Your Personal Medical Records</p>
    </div>

    <div class="band">
      <div class="holder">
        <p class="holder-name">Gareth L. Pomroy</p>
        <p class="holder-title">MD</p>
      </div>

      <ul class="contact">
        <li>
          <svg width="18" height="18" viewBox="0 0 18 18"><circle cx="9" cy="9" r="9" fill="#fff"/><path d="M9 4a3 3 0 0 0-3 3c0 2.3 3 6 3 6s3-3.7 3-6a3 3 0 0 0-3-3zm0 4.2a1.2 1.2 0 1 1 0-2.4 1.2 1.2 0 0 1 0 2.4z" fill="#33229a"/></svg>
          <span>4271 Copper Finch Avenue<br>Denver, Colorado 80219</span>
        </li>
        <li>
          <svg width="18" height="18" viewBox="0 0 18 18"><circle cx="9" cy="9" r="9" fill="#fff"/><path d="M6.3 4.5l1.4 2.2-.9 1a6 6 0 0 0 2.5 2.5l1-.9 2.2 1.4-.6 1.6c-3.6-.3-6.5-3.2-6.8-6.8z" fill="#33229a"/></svg>
          <span>303-555-0148</span>
        </li>
        <li>
          <svg width="18" height="18" viewBox="0 0 18 18"><circle cx="9" cy="9" r="9" fill="#fff"/><rect x="4.5" y="6" width="9" height="6.5" fill="#33229a"/><path d="M4.5 6l4.5 3.6L13.5 6" fill="none" stroke="#fff" stroke-width="1"/></svg>
          <span>garethlpomroy@mailvessel.example</span>
        </li>
        <li>
          <svg width="18" height="18" viewBox="0 0 18 18"><circle cx="9" cy="9" r="9" fill="#fff"/><circle cx="9" cy="9" r="4.8" fill="none" stroke="#33229a" stroke-width="1.2"/><path d="M4.2 9h9.6M9 4.2c-2 2.6-2 7 0 9.6M9 4.2c2 2.6 2 7 0 9.6" fill="none" stroke="#33229a" stroke-width="1"/></svg>
          <span>www.mytamsen.example</span>
        </li>
      </ul>
    </div>
  </div>
</body>
</html>
```